Online Shop - Website Design for up an coming art studio

We require a fully functional website design - not just design - but complete coded online shop website please, which should be a word press style frame work to allow ease up updating the site in the future. The website will sell art work from up and coming artists. The business is called "Copper Harbor Studios". I have attached our logo to allow the submitted designs to tie in with this.

Industry/Entity Type

Shop

Coding

Coded - Design and coding required

Number of Pages Required

1 page

Colors

Designer to choose colors to be used in the design.

Requirements
Must have
• The website design must incorporate and fully functional online eCommerce shop feature.

```html
<!DOCTYPE html>
<html lang="en">
<head>
<meta charset="utf-8">
<title>Copper Harbor Studios</title>
<link href="https://fonts.googleapis.com/css2?family=Jost:wght@400;500&family=Open+Sans:wght@400;600&display=swap" rel="stylesheet">
<style>
:root{
  --crimson:#e31d4b;
  --sky:#27a6df;
  --orange:#f4941f;
  --lime:#8cc63f;
  --ink:#1d1d1d;
  --grey-text:#8a8a8a;
  --panel:#ececec;
  --white:#ffffff;
  --card-title:#2a9fd8;
}
*{box-sizing:border-box;margin:0;padding:0}
html,body{width:1200px;height:2616px;overflow:hidden}
body{position:relative;background:var(--white);font-family:"Open Sans",sans-serif;color:var(--ink)}
.abs{position:absolute}
h1,h2,h3{font-weight:400}

.topbar{left:0;top:0;width:1200px;height:38px;background:var(--crimson);color:var(--white);font-size:13px;display:flex;align-items:center;justify-content:space-between;padding:0 148px 0 116px}
.topbar .address{display:flex;align-items:center;gap:8px}
.topbar .account{font-family:"Jost",sans-serif;font-size:13px;letter-spacing:.3px;display:flex;gap:10px;align-items:center}

.hero{left:0;top:38px;width:1200px;height:672px;background:linear-gradient(100deg,#e8e8e8 0%,#bdbdbd 30%,#d9c0c9 55%,#e7b6c8 70%,#9a9a9a 100%)}
.brand{left:114px;top:66px;display:flex;align-items:center;gap:12px}
.brand-mark{width:80px;height:80px;border-radius:50%;background:#333;flex:none}
.brand-name{font-family:"Jost",sans-serif;font-weight:500;font-size:22px;letter-spacing:.6px;color:#555;text-transform:uppercase;white-space:nowrap}
.nav{left:597px;top:92px;display:flex;gap:28px;font-family:"Jost",sans-serif;font-weight:500;font-size:16px;color:var(--ink)}
.hero-title{left:120px;top:305px;font-family:"Jost",sans-serif;font-weight:400;line-height:1.15}
.hero-title .l1{font-size:46px;color:var(--ink);display:block}
.hero-title .l2{font-size:38px;color:var(--crimson);display:block}
.btn{display:flex;align-items:center;justify-content:center;font-family:"Jost",sans-serif;font-size:18px;color:var(--white)}
.btn-buy{left:122px;top:424px;width:158px;height:47px;background:var(--sky);border:3px solid #bfe6f7}
.dots{left:554px;top:655px;display:flex;gap:8px}
.dots span{width:14px;height:14px;border-radius:50%;background:#111}
.dots span.on{background:transparent;border:2px solid #111}

.welcome-art{left:560px;top:710px;width:565px;height:493px;background:radial-gradient(circle at 52% 48%,#c2185b 0%,#a01a5a 28%,#7d4fa6 42%,#f3ecf6 60%,#ffffff 72%)}
.welcome-title{left:122px;top:815px;font-family:"Jost",sans-serif;font-weight:400;font-size:36px;color:var(--ink);white-space:nowrap;z-index:2}
.welcome-copy{left:129px;top:880px;width:430px;font-size:13.5px;line-height:1.7;color:var(--grey-text);z-index:2}
.welcome-copy p+p{margin-top:12px}
.btn-view{left:129px;top:1039px;width:150px;height:45px;background:var(--orange);border:3px solid #f9c384;font-size:17px}

.featured{left:0;top:1203px;width:1200px;height:541px;background:linear-gradient(180deg,var(--panel) 0%,var(--panel) 62%,#e9b8d0 82%,#f4e3ee 100%)}
.featured-label{left:474px;top:1245px;width:248px;height:47px;border:2px solid var(--crimson);display:flex;align-items:center;justify-content:center;font-family:"Jost",sans-serif;font-size:23px;color:var(--crimson);background:var(--white)}
.card{top:1322px;width:229px;height:312px;background:var(--white);box-shadow:0 1px 3px rgba(0,0,0,.15)}
.card-art{width:229px;height:192px}
.card-title{text-align:center;font-family:"Jost",sans-serif;font-size:21px;color:var(--card-title);margin-top:12px}
.card-artist{text-align:center;font-size:12px;color:var(--grey-text);margin-top:4px}
.card-bar{position:absolute;left:0;bottom:0;width:229px;height:33px;display:flex}
.card-price{width:114px;background:var(--orange);color:var(--white);font-family:"Jost",sans-serif;font-size:21px;display:flex;align-items:center;padding-left:12px}
.card-buy{flex:1;background:var(--lime);color:var(--white);font-size:12px;font-weight:600;display:flex;align-items:center;justify-content:center}
.slider-bar{left:537px;top:1672px;width:112px;height:4px;display:flex;gap:4px}
.slider-bar span{flex:1;background:#bdbdbd}
.slider-bar span.on{background:var(--sky)}

.tiles{left:0;top:1744px;width:1200px;height:480px;background:linear-gradient(180deg,#ffffff 0%,#ffffff 55%,#cfe8f3 78%,#9fd1ea 100%)}
.tile{top:1816px;width:296px;height:333px}
.tile-label{position:absolute;left:50%;transform:translateX(-50%);bottom:38px;border:4px solid var(--white);color:var(--white);font-family:"Jost",sans-serif;font-size:30px;line-height:1.05;text-align:center;text-transform:uppercase;padding:10px 22px;white-space:nowrap}

.footer{left:0;top:2224px;width:1200px;height:392px;background:var(--sky);color:var(--white)}
.footer-brand{left:130px;top:2290px;width:240px;display:flex;flex-direction:column;align-items:center;gap:12px}
.footer-brand .brand-mark{width:76px;height:76px;background:#333}
.footer-brand .brand-name{color:var(--white);font-size:20px;text-align:center;letter-spacing:1.2px}
.col{top:2285px;color:var(--white)}
.col h3{font-family:"Jost",sans-serif;font-weight:400;font-size:23px;margin-bottom:10px}
.col li{list-style:none;font-size:13.5px;line-height:28px;color:#e6f5fc}
.social{display:flex;gap:10px;margin-top:4px}
.social span{width:38px;height:38px;border-radius:50%;background:var(--white)}
.footer-rule{left:172px;top:2541px;width:942px;height:1px;background:rgba(255,255,255,.45)}
.copyright{left:0;top:2563px;width:1200px;text-align:center;font-size:12px;color:#bfe4f5}
</style>
</head>
<body>

<div class="abs topbar">
  <div class="address">
    <svg width="12" height="16" viewBox="0 0 12 16"><path d="M6 0C2.7 0 0 2.6 0 5.9 0 10.3 6 16 6 16s6-5.7 6-10.1C12 2.6 9.3 0 6 0zm0 8.3A2.3 2.3 0 1 1 6 3.7a2.3 2.3 0 0 1 0 4.6z" fill="#fff"/></svg>
    <span>42 Larkfield Lane, Harbourton, Fenshire, Scotland, HB4 7QT</span>
  </div>
  <div class="account">
    <span>MY ACCOUNT</span><span>|</span><span>LOGIN</span><span>|</span><span>MY CART</span>
    <svg width="18" height="15" viewBox="0 0 18 15"><path d="M0 1h3l2.5 8h9L17 3H5" fill="none" stroke="#fff" stroke-width="1.6"/><circle cx="7" cy="13" r="1.5" fill="#fff"/><circle cx="13" cy="13" r="1.5" fill="#fff"/></svg>
  </div>
</div>

<section class="abs hero" role="img" aria-label="Painted street scene in grey and pink with a tower, a blossoming tree and a couple under a lamp post"></section>

<div class="abs brand">
  <span class="brand-mark"></span>
  <span class="brand-name">Copper Harbor Studios</span>
</div>
<nav class="abs nav">
  <span>ABOUT</span><span>ART WORK</span><span>SHOP NOW</span><span>BLOG</span><span>CONTACT</span>
</nav>
<h1 class="abs hero-title">
  <span class="l1">GET GREAT ART WORK</span>
  <span class="l2">FROM GRETEST ARTISTS</span>
</h1>
<div class="abs btn btn-buy">BUY NOW</div>
<div class="abs dots"><span class="on"></span><span></span><span></span><span></span></div>

<div class="abs welcome-art" role="img" aria-label="Round magenta and gold marbled artwork framed by purple watercolour flowers"></div>
<h2 class="abs welcome-title">Welcome to Our Website</h2>
<div class="abs welcome-copy">
  <p>Praesent elementum elit at tellus nec ultricies sit amet porttitor mattis enim In massa libero interdum nec interdum</p>
  <p>vel blandit sed nulla In ullamcorper est eget tempor cursus neque mi consectetuer mi a ultricies massa est sed nisl Class aptent taciti sociosqu ad litora torquent</p>
</div>
<div class="abs btn btn-view">View Work</div>

<section class="abs featured" role="img" aria-label="Light grey panel fading into pink watercolour splashes"></section>
<div class="abs featured-label">Featured Arts</div>

<article class="abs card" style="left:115px">
  <div class="card-art" role="img" aria-label="Colourful expressive oil painting in orange, green and red" style="background:linear-gradient(135deg,#d9772f,#3b5a2a 55%,#c03a2b)"></div>
  <div class="card-title">Art Work Tittle</div>
  <div class="card-artist">By Artists Name</div>
  <div class="card-bar"><span class="card-price">$256</span><span class="card-buy">Buy Now</span></div>
</article>
<article class="abs card" style="left:366px">
  <div class="card-art" role="img" aria-label="Painting of a purple forest with a deer in a green meadow" style="background:linear-gradient(180deg,#7b3fa0,#5b2f8a 55%,#3fa87a)"></div>
  <div class="card-title">Art Work Tittle</div>
  <div class="card-artist">By Artists Name</div>
  <div class="card-bar"><span class="card-price">$256</span><span class="card-buy">Buy Now</span></div>
</article>
<article class="abs card" style="left:607px">
  <div class="card-art" role="img" aria-label="Deep blue and violet abstract floral painting" style="background:linear-gradient(135deg,#1a2f8c,#5a2fa0 50%,#152050)"></div>
  <div class="card-title">Art Work Tittle</div>
  <div class="card-artist">By Artists Name</div>
  <div class="card-bar"><span class="card-price">$256</span><span class="card-buy">Buy Now</span></div>
</article>
<article class="abs card" style="left:853px">
  <div class="card-art" role="img" aria-label="Warm watercolour sketch of a domed cathedral" style="background:linear-gradient(180deg,#e9d6c6,#b99378 60%,#8a7a70)"></div>
  <div class="card-title">Art Work Tittle</div>
  <div class="card-artist">By Artists Name</div>
  <div class="card-bar"><span class="card-price">$256</span><span class="card-buy">Buy Now</span></div>
</article>
<div class="abs slider-bar"><span></span><span></span><span class="on"></span></div>

<section class="abs tiles" role="img" aria-label="White panel with a blue watercolour wash along the lower edge"></section>
<div class="abs tile" style="left:117px;background:linear-gradient(135deg,#111 0%,#3a2a6a 40%,#d8822f 70%,#2d9fd0 100%)" role="img" aria-label="Abstract profile made of colourful flowing strands">
  <span class="tile-label">Popular<br>Art</span>
</div>
<div class="abs tile" style="left:448px;background:linear-gradient(180deg,#e07a86,#d9475a 60%,#b8303f)" role="img" aria-label="Red-toned painting of a tower behind blossoming trees">
  <span class="tile-label">From Our<br>Blogs</span>
</div>
<div class="abs tile" style="left:785px;background:linear-gradient(135deg,#cfc5b0,#3fa6a0 50%,#c9502f)" role="img" aria-label="Painting of red autumn branches against a teal sky">
  <span class="tile-label">Our<br>Artists</span>
</div>

<footer class="abs footer"></footer>
<div class="abs footer-brand">
  <span class="brand-mark"></span>
  <span class="brand-name">Copper Harbor Studios</span>
</div>
<div class="abs col" style="left:415px">
  <h3>Quick Links</h3>
  <ul><li>Home</li><li>About</li><li>Our Art</li><li>Shop Now</li><li>Blogs</li></ul>
</div>
<div class="abs col" style="left:586px">
  <h3>Resources</h3>
  <ul><li>My Account</li><li>My Cart</li><li>Wishlist</li><li>Support</li><li>Contact</li></ul>
</div>
<div class="abs col" style="left:759px">
  <h3>Sublinks</h3>
  <ul><li>Our Artists</li><li>Most Popular</li><li>Why Us</li><li>Testimonials</li></ul>
</div>
<div class="abs col" style="left:903px">
  <h3>Stay in Touch</h3>
  <div class="social"><span></span><span></span><span></span><span></span></div>
</div>
<div class="abs footer-rule"></div>
<div class="abs copyright">© 2017 Company Name. All right reserved</div>

</body>
</html>
```